IT Management and Consulting company wants a design

The website should transfer an innovative, forward-oriented, optimistic, and serious image to my customer. Because we work in an agile, the design should transfer this approach.

The new color should make a serious, but not boring, impression for the business visitors of top-level companies.

The main focus topics are:
* IT strategy consulting
* Digital transformation
* IT quality management

The website should be in the English language.

The website should be created for WordPress. The existing website is http://www.t-vork.com (no WordPress) is provided by servalpin.de. A WordPress sandbox system exists.

Target Market(s)

Purchasing departments, IT decision makers from companies, project recruiting companies

Industry/Entity Type

IT-Provider, Telecommunication, Automotive

Coding

Coded - Design and coding required

Number of Pages Required

4 page

Font styles to use
Serif
Sans Serif

Requirements
Must have
• Long-pager scrolling, a detail page for each portfolio topics, contact page, page about the company
Nice to have
• Parallax animation less is more, maybe a nice Hero Video Header, interessting 3D graph, Isometric graphs will bi nice, more clean than overloaded,
Should not have
• personal recruting page like in www.t-vork.com

```html
<!DOCTYPE html>
<html lang="en">
<head>
<meta charset="utf-8">
<title>Veyra Consulting – IT Management and Consulting</title>
<link rel="stylesheet" href="https://fonts.googleapis.com/css2?family=Barlow:wght@400;600;700&family=Saira:wght@300;400;500;600;700&family=Poppins:wght@300;400;500;600&family=Roboto+Slab:wght@400;500;700&display=swap">
<style>
:root{
  --gold:#b8860b;
  --gold-dark:#a27508;
  --ink:#222;
  --text:#555;
  --muted:#888;
  --grey:#e6e6e6;
  --cream:#f6f0e3;
  --navy:#0f1622;
  --white:#fff;
}
*{margin:0;padding:0;box-sizing:border-box}
html,body{width:1200px;height:4542px;overflow:hidden}
body{position:relative;font-family:"Poppins",sans-serif;color:var(--text);background:var(--white)}
.abs{position:absolute}
.gold{color:var(--gold)}

/* header */
.header{left:0;top:0;width:1200px;height:74px;background:#fff}
.brand{left:62px;top:24px;display:flex;align-items:center;gap:10px}
.brand-mark{width:10px;height:10px;background:var(--gold)}
.brand-name{font-family:"Poppins",sans-serif;font-size:20px;font-weight:500;color:var(--ink);line-height:24px}
.nav{left:545px;top:30px;display:flex;gap:19px;font-size:12px;color:#555}
.nav .active{color:var(--gold)}
.phone-btn{left:914px;top:18px;width:226px;height:40px;border-radius:20px;background:var(--gold);color:#fff;font-size:15px;display:flex;align-items:center;gap:10px;padding-left:8px}
.phone-ico{width:28px;height:28px;border-radius:50%;background:#fff;display:flex;align-items:center;justify-content:center}

/* hero */
.hero{left:0;top:74px;width:1200px;height:638px;background:radial-gradient(ellipse at 70% 40%,#2d5c7a 0%,#12263a 45%,#060c14 100%)}
.hero h1{left:60px;top:188px;font-family:"Barlow",sans-serif;font-weight:700;font-size:46px;line-height:52px;color:#fff}
.hero .lead{left:62px;top:362px;font-size:15px;color:#fff}
.play{left:60px;top:424px;display:flex;align-items:center;gap:18px;color:var(--gold);font-size:15px}
.play-circle{width:62px;height:62px;border:2px solid var(--gold);border-radius:50%;display:flex;align-items:center;justify-content:center}

/* bands */
.band-gold{left:0;top:712px;width:1200px;height:74px;background:var(--gold)}
.gold-square{left:937px;top:786px;width:263px;height:165px;background:var(--gold)}
.expert{left:0;top:786px;width:937px;height:507px;background:var(--grey)}
.sec-title{font-family:"Saira",sans-serif;font-size:30px;color:var(--gold);font-weight:400;text-align:center}
.sec-title b{font-weight:700}
.expert .sec-title{left:0;top:66px;width:1200px}
.expert .intro{left:370px;top:128px;width:460px;font-size:12px;line-height:21px;text-align:center}
.card{width:276px;height:233px;background:#fff;border-radius:8px;box-shadow:0 2px 10px rgba(0,0,0,.08)}
.card .pic{position:absolute;left:18px;top:0;width:240px;height:160px;border-radius:4px 4px 0 0}
.card .label{position:absolute;left:0;top:176px;width:100%;text-align:center;font-family:"Roboto Slab",serif;font-size:17px;line-height:21px;color:var(--ink)}

/* company */
.big-word{left:0;top:1650px;font-family:"Roboto Slab",serif;font-weight:700;font-size:190px;color:#f5f2ec;line-height:1}
.company-h{left:601px;top:1405px;font-family:"Saira",sans-serif;font-size:36px;color:var(--gold);font-weight:600}
.company-sub{left:604px;top:1455px;font-size:12px;color:var(--muted)}
.company-method{left:606px;top:1486px;font-family:"Roboto Slab",serif;font-size:15px;font-weight:500;color:var(--gold)}
.company-text{left:604px;top:1519px;width:380px;font-size:11.5px;line-height:19.5px}
.company-text p{margin-bottom:12px}
.learn{left:604px;top:1686px;font-size:13px;color:var(--gold);text-decoration:underline;font-weight:500}
.years{left:310px;top:1548px;text-align:center;color:var(--gold);font-family:"Saira",sans-serif}

/* mission */
.mission-bg{left:0;top:1815px;width:1200px;height:384px;background:var(--cream)}
.mbox{top:1894px;height:194px;background:#fff;text-align:center}
.mbox .ico{margin:0 auto;width:92px;height:104px;background:var(--gold);display:flex;align-items:center;justify-content:center}
.mbox .cap{margin-top:38px;font-size:16px;font-weight:500;letter-spacing:.5px;color:#333}
.mbox.feature{background:var(--gold-dark);color:#fff;font-family:"Roboto Slab",serif;font-weight:500;font-size:16px;line-height:21px;padding:28px 24px 0}

/* about */
.about{left:0;top:2199px;width:974px;height:396px;background:linear-gradient(100deg,#0b111a 0%,#13202e 60%,#1c2c3d 100%)}
.about-photo{left:650px;top:0;width:324px;height:396px;background:radial-gradient(ellipse at 50% 45%,#4b5563 0%,#1b2633 75%)}
.about h2{left:162px;top:66px;font-family:"Saira",sans-serif;font-size:28px;color:#fff;font-weight:500}
.about h2 span{font-weight:300}
.about .txt{left:162px;width:370px;font-size:11px;line-height:19px;color:#eee}
.about .quote{left:126px;top:177px;width:414px;height:48px;background:var(--gold);color:#fff;font-size:13px;line-height:19px;padding:5px 0 0 36px}

/* portfolio */
.portfolio-h{left:0;top:2666px;width:1200px;text-align:center;font-family:"Saira",sans-serif;font-size:34px;color:var(--gold);font-weight:600}
.portfolio-sub{left:0;top:2718px;width:1200px;text-align:center;font-size:13px;color:#333}
.portfolio-intro{left:360px;top:2757px;width:480px;text-align:center;font-size:12px;line-height:21px}
.slide{top:2863px;height:353px}
.slide-caption{left:300px;top:3134px;width:360px;height:82px;background:rgba(20,26,34,.75);padding:14px 0 0 36px;color:#fff}
.slide-caption h3{font-family:"Saira",sans-serif;font-size:22px;font-weight:600}
.slide-caption p{font-size:11px}
.arrow-btn{width:44px;height:44px;background:var(--gold);display:flex;align-items:center;justify-content:center}

/* news */
.news{left:226px;top:3291px;width:974px;height:374px;background:var(--gold)}
.news-pic{left:243px;top:3309px;width:338px;height:338px;background:radial-gradient(ellipse at 55% 55%,#5ea6d6 0%,#1f4766 45%,#0b1826 100%)}
.news h2{left:443px;top:98px;font-family:"Saira",sans-serif;font-size:30px;color:#fff;letter-spacing:2px;font-weight:600}
.news p{left:443px;top:146px;width:420px;font-size:12px;line-height:21px;color:#fff}
.news .yr{left:592px;top:240px;font-family:"Saira",sans-serif;font-size:130px;font-weight:700;color:rgba(0,0,0,.06);line-height:1}
.news-nav{left:443px;top:262px;display:flex;gap:10px}
.news-nav span{width:36px;height:36px;border:1.5px solid #fff;display:flex;align-items:center;justify-content:center}
.grey-bar{background:var(--grey)}

/* contact */
.contact-h{left:217px;top:3742px;font-family:"Saira",sans-serif;font-size:34px;color:var(--gold);font-weight:300}
.contact-h b{font-weight:700}
.contact-sub{left:217px;top:3794px;font-size:13px;color:#333}
.field{left:217px;width:379px;height:40px;border:1px solid #ddd;border-radius:3px;font-size:11px;color:#666;padding:11px 14px}
.submit{left:217px;top:4105px;width:118px;height:40px;background:var(--gold);color:#fff;font-weight:600;letter-spacing:1px;font-size:14px;display:flex;align-items:center;justify-content:center;border-radius:4px}
.contact-photo{left:758px;top:3753px;width:387px;height:467px;background:radial-gradient(ellipse at 55% 45%,#e9e4dc 0%,#f7f5f1 70%,#fff 100%)}

/* footer */
.footer{left:0;top:4220px;width:1200px;height:273px;background:var(--navy)}
.footer .brand-name{color:#fff}
.footer h4{font-size:15px;color:var(--gold);font-weight:500;letter-spacing:.5px}
.footer ul{list-style:none;margin-top:12px;font-size:11px;color:#ddd;line-height:26px}
.footer ul li::before{content:"";display:inline-block;width:5px;height:5px;border-radius:50%;background:var(--gold);margin-right:12px;vertical-align:middle}
.f-contact{font-size:11px;color:#ddd;line-height:20px}
.f-row{display:flex;gap:14px;margin-top:12px}
.copy{left:0;top:4493px;width:1200px;height:49px;background:var(--gold);color:#f3e3c0;font-size:12px;display:flex;align-items:center;justify-content:center}
</style>
</head>
<body>

<!-- Header -->
<header class="abs header">
  <div class="abs brand"><span class="brand-mark"></span><span class="brand-name">Veyra Consulting</span></div>
  <nav class="abs nav"><span class="active">Home</span><span>Companies</span><span>Portfolio</span><span>Scouting</span><span>Contact Us</span></nav>
  <div class="abs phone-btn"><span class="phone-ico"><svg width="16" height="16" viewBox="0 0 24 24"><path d="M6.6 10.8a15 15 0 006.6 6.6l2.2-2.2c.3-.3.7-.4 1-.2 1.1.4 2.3.6 3.6.6.6 0 1 .4 1 1V20c0 .6-.4 1-1 1C10.6 21 3 13.4 3 4c0-.6.4-1 1-1h3.5c.6 0 1 .4 1 1 0 1.3.2 2.5.6 3.6.1.3 0 .7-.2 1z" fill="#b8860b"/></svg></span>+49 (0) 8100 5550188</div>
</header>

<!-- Hero -->
<section class="abs hero" role="img" aria-label="Woman touching a glowing circuit board display in a dark room">
  <h1 class="abs">In <span class="gold">Compliance</span> With<br>All Time And Cost<br>Specifications.</h1>
  <p class="abs lead">Automotive and Telecommunications Consulting Services.</p>
  <div class="abs play"><span class="play-circle"><svg width="20" height="22" viewBox="0 0 20 22"><path d="M2 1l17 10L2 21z" fill="#b8860b"/></svg></span>Watch Video</div>
</section>

<div class="abs band-gold"></div>
<div class="abs gold-square"></div>
<svg class="abs" style="left:1010px;top:712px" width="190" height="190" viewBox="0 0 190 190"><g fill="#c99a2e"><rect x="88" y="0" width="14" height="62"/><rect x="88" y="118" width="14" height="72"/><rect x="4" y="88" width="70" height="14"/><rect x="120" y="88" width="70" height="14"/></g></svg>

<!-- Expertise -->
<section class="abs expert">
  <h2 class="abs sec-title"><b>We Are</b> Expert In</h2>
  <p class="abs intro">Veyra Consulting you create the best conditions for IT systems that do what they should. In compliance with all time and cost specifications.</p>
</section>
<div class="abs card" style="left:162px;top:983px"><div class="pic" role="img" aria-label="Red rising bar chart arrow on dark background" style="background:linear-gradient(160deg,#3a0d10,#0e0e12)"></div><div class="label">IT Strategy<br>Consulting</div></div>
<div class="abs card" style="left:462px;top:983px"><div class="pic" role="img" aria-label="Hand touching a digital data interface" style="background:linear-gradient(160deg,#1b2a55,#07091a)"></div><div class="label gold">Digital<br>Transformation</div></div>
<div class="abs card" style="left:761px;top:983px"><div class="pic" role="img" aria-label="Colourful three-dimensional statistics chart illustration" style="background:linear-gradient(180deg,#7fb7cf 0%,#6aa8c2 75%,#1a8f8a 100%)"></div><div class="label">IT Quality<br>Management</div></div>

<!-- Company -->
<div class="abs big-word">Veyra</div>
<div class="abs" role="img" aria-label="Engineers with a holographic wireframe car" style="left:162px;top:1404px;width:150px;height:147px;background:linear-gradient(150deg,#2d6f96,#0c2235)"></div>
<div class="abs" style="left:323px;top:1410px;width:27px;height:124px;background:#9a9a9a"></div>
<div class="abs" style="left:170px;top:1565px;width:124px;height:27px;background:var(--gold)"></div>
<div class="abs" style="left:380px;top:1565px;width:124px;height:27px;background:var(--gold)"></div>
<div class="abs" style="left:323px;top:1622px;width:27px;height:124px;background:#9a9a9a"></div>
<div class="abs" role="img" aria-label="Telecommunication antenna tower at night" style="left:361px;top:1603px;width:150px;height:150px;background:linear-gradient(180deg,#1a2640,#05070c)"></div>
<div class="abs years"><div style="font-size:38px;line-height:38px;font-weight:600">25</div><div style="font-size:12px">Years</div></div>
<h2 class="abs company-h">Veyra Consulting</h2>
<div class="abs company-sub">Power of Cometence</div>
<div class="abs company-method">Professional Method For Project Success</div>
<div class="abs company-text">
  <p>Whether IT project management, consulting, commissioning management or system integration: With Veyra Consulting you create the best conditions for IT systems that do what they should. In compliance with all time and cost specifications.</p>
  <p>Well-known companies from the automotive &amp; telecommunications industries regularly use our know-how in the form of individual management and consulting services.</p>
</div>
<div class="abs learn">LEARN MORE &nbsp;›</div>

<!-- Mission -->
<div class="abs mission-bg"></div>
<div class="abs mbox" style="left:217px;width:239px">
  <div class="ico"><svg width="60" height="60" viewBox="0 0 60 60" fill="none" stroke="#fff" stroke-width="2.5"><circle cx="30" cy="30" r="24"/><path d="M22 20a7 7 0 0114 0c0 6-7 13-7 13s-7-7-7-13z"/><circle cx="29" cy="20" r="2.5"/><path d="M36 36a5 5 0 0110 0c0 4-5 9-5 9s-5-5-5-9z"/></svg></div>
  <div class="cap">LOCATIONS</div>
</div>
<div class="abs mbox feature" style="left:479px;width:242px">Our Mission is to Carry out Complex Projects Efficiently with high Quality for the Benefit of Our Customers. - Transparent, Reliable, Agile</div>
<div class="abs mbox" style="left:742px;width:239px">
  <div class="ico"><svg width="60" height="60" viewBox="0 0 60 60" fill="none" stroke="#fff" stroke-width="2.5"><circle cx="20" cy="18" r="7"/><circle cx="40" cy="18" r="7"/><path d="M8 52v-8a10 10 0 0110-10h4M52 52v-8a10 10 0 00-10-10h-4M22 30l8 8 8-8"/></svg></div>
  <div class="cap">PARTNERS</div>
</div>

<!-- About -->
<section class="abs about">
  <div class="abs about-photo" role="img" aria-label="Portrait of the company founder in a suit with arms crossed"></div>
  <div class="abs" style="left:52px;top:0;width:48px;height:110px;background:var(--gold)"></div>
  <div class="abs" style="left:0;top:184px;width:26px;height:40px;background:var(--gold)"></div>
  <div class="abs" style="left:52px;top:250px;width:48px;height:146px;background:var(--gold)"></div>
  <h2 class="abs">About <span>Martin</span></h2>
  <p class="abs txt" style="top:116px">Veyra Consulting GmbH was founded by Martin Keller in 2010 and has been operating successfully on the market ever since.</p>
  <div class="abs quote">Use guarantee of success: Concentration on the essentials, customer orientation and experience</div>
  <p class="abs txt" style="top:240px">Thanks to more than 25 years of activity in project management and consulting, mainly for medium-sized and large companies, Veyra Consulting is very familiar with the challenges in all project phases of complex IT projects.</p>
</section>

<!-- Portfolio -->
<h2 class="abs portfolio-h">Portfolio</h2>
<div class="abs portfolio-sub">Aur The Essential Focus</div>
<p class="abs portfolio-intro">Our range of services covers the management of the entire development process from applications and extensions to quality assurance through to going live and support afterwards.</p>
<div class="abs slide" role="img" aria-label="Hands typing on a laptop with a cloud lock overlay" style="left:0;width:247px;background:linear-gradient(150deg,#5d6f80,#1d2a36)"></div>
<div class="abs slide" role="img" aria-label="Engineer with laptop next to an industrial robot arm" style="left:300px;width:600px;background:linear-gradient(120deg,#8a9aa8 0%,#4f6374 55%,#1e2a35 100%)"></div>
<div class="abs slide" role="img" aria-label="Person holding a smartphone with charts" style="left:951px;width:249px;background:linear-gradient(150deg,#2c3f55,#0c1520)"></div>
<div class="abs slide-caption"><h3>DIgitlization</h3><p>The digital upheaval is a reality and in full swing.</p></div>
<div class="abs arrow-btn" style="left:226px;top:3018px"><svg width="14" height="20" viewBox="0 0 14 20"><path d="M11 2L3 10l8 8" stroke="#fff" stroke-width="2" fill="none"/></svg></div>
<div class="abs arrow-btn" style="left:931px;top:3018px"><svg width="14" height="20" viewBox="0 0 14 20"><path d="M3 2l8 8-8 8" stroke="#fff" stroke-width="2" fill="none"/></svg></div>

<!-- News -->
<div class="abs grey-bar" style="left:185px;top:3291px;width:30px;height:140px"></div>
<div class="abs grey-bar" style="left:15px;top:3463px;width:138px;height:30px"></div>
<div class="abs grey-bar" style="left:185px;top:3525px;width:30px;height:140px"></div>
<section class="abs news">
  <h2 class="abs">NEWS</h2>
  <p class="abs">Veyra Consulting is carrying out a change project. The central test team for user acceptance tests will be transferred to the squad structure of the agile organization of the Open Nimbus Cloud (ONC). As part of this project, Trackly / Testora will be introduced as a strategic test tool in the ONC organization</p>
  <div class="abs news-nav"><span><svg width="10" height="14" viewBox="0 0 10 14"><path d="M8 1L2 7l6 6" stroke="#fff" stroke-width="1.8" fill="none"/></svg></span><span><svg width="10" height="14" viewBox="0 0 10 14"><path d="M2 1l6 6-6 6" stroke="#fff" stroke-width="1.8" fill="none"/></svg></span></div>
  <div class="abs yr">2020</div>
</section>
<div class="abs news-pic" role="img" aria-label="Hand holding a glowing holographic car with dashboard interface"></div>

<!-- Contact -->
<div class="abs grey-bar" style="left:846px;top:3665px;width:40px;height:185px"></div>
<div class="abs grey-bar" style="left:626px;top:3900px;width:178px;height:40px"></div>
<div class="abs grey-bar" style="left:928px;top:3900px;width:178px;height:40px"></div>
<div class="abs contact-photo" role="img" aria-label="Cheerful man in a white shirt pointing to the contact form"></div>
<h2 class="abs contact-h"><b>Please</b> Contact Us !</h2>
<div class="abs contact-sub">Need an have Any Question for Contact us Today !</div>
<div class="abs field" style="top:3834px">Name *</div>
<div class="abs field" style="top:3888px">Reference *</div>
<div class="abs field" style="top:3941px">Email *</div>
<div class="abs field" style="top:3996px;height:97px">Message *</div>
<div class="abs submit">SUBMIT</div>

<!-- Footer -->
<footer class="abs footer">
  <div class="abs brand" style="left:70px;top:116px"><span class="brand-mark"></span><span class="brand-name">Veyra Consulting</span></div>
  <div class="abs" style="left:337px;top:46px"><h4>SITEMAP</h4><ul><li>Home</li><li>Companies</li><li>Portfolio</li><li>Scouting</li><li>Contact Us</li></ul></div>
  <div class="abs" style="left:612px;top:46px"><h4>EXPERT IN</h4><ul><li>IT strategy consulting</li><li>Digital transformation</li><li>IT quality management</li></ul></div>
  <div class="abs" style="left:887px;top:46px;width:240px"><h4>CONTACT US</h4>
    <div class="f-row f-contact"><svg width="14" height="18" viewBox="0 0 14 18"><path d="M7 1a6 6 0 016 6c0 5-6 10-6 10S1 12 1 7a6 6 0 016-6z" fill="#b8860b"/><circle cx="7" cy="7" r="2" fill="#0f1622"/></svg><span>Veyra Consulting GmbH<br>Werkstraße 12 - 14 D-80001<br>Lindenau</span></div>
    <div class="f-row f-contact"><svg width="14" height="14" viewBox="0 0 24 24"><path d="M6.6 10.8a15 15 0 006.6 6.6l2.2-2.2c.3-.3.7-.4 1-.2 1.1.4 2.3.6 3.6.6.6 0 1 .4 1 1V20c0 .6-.4 1-1 1C10.6 21 3 13.4 3 4c0-.6.4-1 1-1h3.5c.6 0 1 .4 1 1 0 1.3.2 2.5.6 3.6.1.3 0 .7-.2 1z" fill="#b8860b"/></svg><span>+49 (0) 8100 5550188<br>+49 (0) 8100 5550189</span></div>
    <div class="f-row f-contact"><svg width="14" height="12" viewBox="0 0 14 12"><rect x="0.5" y="0.5" width="13" height="11" fill="#b8860b"/><path d="M1 1l6 5 6-5" stroke="#0f1622" fill="none"/></svg><span>info@t-vork.com</span></div>
  </div>
</footer>
<div class="abs copy">©2021 Veyra Consulting GmbH - All right reserved</div>

</body>
</html>
```